*** Business Card Design Project

I need a logo and business card for my new catering business: "Pomelia". The design should be modern, clean, elegant and refined. One or Two colours only. The design SHOULD NOT include graphics or images. There should be space for my name, phone number and email address (I will provide these to you later).

Industry/Entity Type

Catering

Requirements
Must have
• Must have one or two colours only.
Must include the text "pomelia"
Should not have
• Must not have graphics or images.

```html
<!DOCTYPE html>
<html lang="en">
<head>
<meta charset="utf-8">
<title>Pomelia – Business Card</title>
<link rel="stylesheet" href="https://fonts.googleapis.com/css2?family=Gabriela&display=swap">
<style>
  :root {
    --card-bg: #c3cfb9;
    --ink-dark: #1e2e17;
    --ink-green: #45703a;
    --mark-green: #4b7a3c;
  }
  html, body {
    margin: 0;
    padding: 0;
    width: 1200px;
    height: 741px;
    overflow: hidden;
    background: var(--card-bg);
  }
  .card {
    position: relative;
    width: 1200px;
    height: 741px;
    background: var(--card-bg);
    font-family: "Gabriela", Georgia, serif;
    color: var(--ink-dark);
  }
  .brand-dot {
    position: absolute;
    left: 190px;
    top: 150px;
    width: 130px;
    height: 130px;
    border-radius: 50%;
    background: var(--mark-green);
  }
  .brand-name {
    position: absolute;
    left: 345px;
    top: 110px;
    margin: 0;
    font-size: 150px;
    line-height: 1;
    font-weight: 400;
    color: var(--ink-dark);
    letter-spacing: 1px;
  }
  .contact {
    position: absolute;
    left: 0;
    width: 1236px;
    text-align: center;
    margin: 0;
    line-height: 1;
  }
  .contact-name {
    top: 382px;
    font-size: 60px;
    color: var(--ink-green);
  }
  .contact-phone {
    top: 452px;
    font-size: 44px;
  }
  .contact-email {
    top: 556px;
    font-size: 46px;
  }
</style>
</head>
<body>
  <main class="card">
    <span class="brand-dot" aria-hidden="true"></span>
    <h1 class="brand-name">Pomelia</h1>
    <p class="contact contact-name">Your Name</p>
    <p class="contact contact-phone">01234 567 890</p>
    <p class="contact contact-email">email@address.com</p>
  </main>
</body>
</html>
```